Fast Growing Personal Injury Law Firm Needs Business Card Design

We need a business card design for a fast growing personal injury law firm in Florida. Our name is Darren Kolvisty, P.A. Our practice is comprised of younger attorneys (in their 30s) that employ more modern techniques/tools than our older competition. We would prefer a look that is a modern play on a classic look. Also, we would like to continue using a color scheme that employs navy blue and kelly green (other shades of green could be fine too) as well as our "E" logo.

Industry/Entity Type

Law Firm

```html
<!DOCTYPE html>
<html lang="en">
<head>
<meta charset="utf-8">
<title>Darren Kolvisty, P.A. — Business Card</title>
<link href="https://fonts.googleapis.com/css2?family=Crimson+Pro:ital,wght@0,700;1,500&family=PT+Sans:ital,wght@0,400;0,700;1,700&display=swap" rel="stylesheet">
<style>
  :root {
    --navy: #1d2d5e;
    --green: #1f8a3f;
    --stage: #000000;
    --paper: #ffffff;
    --paper-edge: #e9e9ec;
    --rule: #e6e6e8;
  }
  * { margin: 0; padding: 0; box-sizing: border-box; }
  html, body { width: 1057px; height: 1200px; overflow: hidden; background: var(--stage); }
  .canvas { position: relative; width: 1057px; height: 1200px; }

  .card { position: absolute; left: 135px; width: 787px; height: 450px; background: var(--paper); }
  .card--front { top: 135px; background: radial-gradient(ellipse at 50% 45%, #ffffff 35%, var(--paper-edge) 100%); }
  .card--back { top: 615px; }

  .brand-mark { position: absolute; background: var(--navy); }
  .card--front .brand-mark { left: 313px; top: 113px; width: 163px; height: 140px; }
  .card--back .brand-mark { left: 141px; top: 146px; width: 114px; height: 97px; }

  .firm-name {
    position: absolute; left: 0; width: 100%; text-align: center;
    font-family: "Crimson Pro", Georgia, serif; font-weight: 700;
    color: var(--navy); text-transform: uppercase; letter-spacing: 0.2px; line-height: 1;
  }
  .tagline {
    position: absolute; display: flex; align-items: center; gap: 8px;
    font-family: "Crimson Pro", Georgia, serif; font-style: italic; font-weight: 500;
    color: var(--green); line-height: 1; white-space: nowrap;
  }
  .tagline::before, .tagline::after { content: ""; flex: 1; height: 1px; background: var(--green); }

  .card--front .firm-name { top: 283px; font-size: 33px; }
  .card--front .tagline { left: 193px; width: 404px; top: 316px; font-size: 24px; }

  .lockup-back { position: absolute; left: 0; top: 0; width: 394px; height: 450px; }
  .card--back .firm-name { top: 262px; font-size: 23px; }
  .card--back .tagline { left: 57px; width: 282px; top: 286px; font-size: 17px; }

  .divider { position: absolute; left: 393px; top: 50px; width: 2px; height: 348px;
    background: linear-gradient(to bottom, transparent, var(--rule) 15%, var(--rule) 85%, transparent); }

  .contact { position: absolute; left: 451px; top: 140px; font-family: "PT Sans", Arial, sans-serif; color: var(--navy); }
  .contact__name { font-size: 25px; font-weight: 700; line-height: 1; }
  .contact__role { margin-top: 6px; font-size: 14px; font-weight: 700; font-style: italic; }
  .contact__list { list-style: none; margin-top: 28px; font-size: 15px; line-height: 18px; }
  .contact__list li { display: flex; align-items: flex-start; gap: 8px; margin-bottom: 2px; }
  .contact__list svg { width: 12px; height: 12px; margin-top: 3px; flex: none; fill: var(--green); }
</style>
</head>
<body>
<div class="canvas">

  <section class="card card--front">
    <div class="brand-mark"></div>
    <div class="firm-name">Darren Kolvisty, P.A.</div>
    <div class="tagline">personal injury attorneys</div>
  </section>

  <section class="card card--back">
    <div class="lockup-back">
      <div class="brand-mark"></div>
      <div class="firm-name">Darren Kolvisty, P.A.</div>
      <div class="tagline">personal injury attorneys</div>
    </div>
    <div class="divider"></div>
    <div class="contact">
      <div class="contact__name">Darren Kolvisty</div>
      <div class="contact__role">attorney at law</div>
      <ul class="contact__list">
        <li><svg viewBox="0 0 12 12"><path d="M6 0a4.2 4.2 0 0 0-4.2 4.2C1.8 7.3 6 12 6 12s4.2-4.7 4.2-7.8A4.2 4.2 0 0 0 6 0zm0 6a1.8 1.8 0 1 1 0-3.6A1.8 1.8 0 0 1 6 6z"/></svg>
          <span>2150 Harbor Point Drive Suite 410<br>Bradenton Shores, FL 34209</span></li>
        <li><svg viewBox="0 0 12 12"><path d="M0 4c0-2 2.5-3 6-3s6 1 6 3v1H9V3.5H3V5H0zM2 6h8l1 5H1zm4 1.2a1.6 1.6 0 1 0 0 3.2 1.6 1.6 0 0 0 0-3.2z"/></svg><span>555-214-3870</span></li>
        <li><svg viewBox="0 0 12 12"><path d="M3 0h6v3H3zM0 4h12v5h-2V7H2v2H0zm2.5 4h7v4h-7z"/></svg><span>555-214-3871</span></li>
        <li><svg viewBox="0 0 12 12"><path d="M0 2h12v1L6 7 0 3zm0 2.3 6 4 6-4V10H0z"/></svg><span>darren@kolvistylaw.com</span></li>
        <li><svg viewBox="0 0 12 12"><path d="M6 0a6 6 0 1 0 0 12A6 6 0 0 0 6 0zm0 1.3a4.7 4.7 0 0 1 4.6 3.9H8.4C8.2 3.5 7.3 2 6 1.3zm-1.3.2C4 2.3 3.7 3.6 3.6 5.2H1.4a4.7 4.7 0 0 1 3.3-3.7zM1.4 6.8h2.2c.1 1.6.5 2.9 1.1 3.7a4.7 4.7 0 0 1-3.3-3.7zm7 0h2.2a4.7 4.7 0 0 1-4.6 3.9c1.3-.7 2.2-2.2 2.4-3.9z"/></svg><span>www.kolvistylaw.com</span></li>
      </ul>
    </div>
  </section>

</div>
</body>
</html>
```